International Freight Forwarder need a business card

We need a logo design for a freight forwarding company . We are active in Sea Transportation, Truck transportation, and Air Transportation, The design should be have normal dimensions of a card and should not have cuts and holes in its design (printed design is required - lamination accepted)

The said company is agent and sales representative of 2 other Shipping companies (whose logos, name, and website should also be mentioned on the card)

Industry/Entity Type

Logistics

Contact Information for Business Card

Address is "No.7, 2nd Sarv Baghestan-e-Nouri, Tehran, IR
Tel number is +98 21 66394512
Fax number is +98 21 66395830
E-Mail address is info@roshanbarsaz.com
Website is www.roshanbarsaz.com

Open Layer Logos attached as well

Colors
33a6d7
0292cd
0255a3
3276b5
85abd2
85cae6
cee9f5
d5e2ee
ffffff

Requirements
Must have
• Main logo of Roshan Barsaz
• Logo of TQM Shipping Line
• London, United Kingdom
• tqmline.com
• Logo of Calm Reef Shipping
• Dubai, United Arab Emirates
• crsuae.com
• We require OPEN layer file to be submitted to us upon project selection.
Should not have
• Weird Designs such as cuts to the shape or holes in design.

```html
<!DOCTYPE html>
<html lang="en">
<head>
<meta charset="utf-8">
<title>Roshan Barsaz – Business Card</title>
<link rel="stylesheet" href="https://fonts.googleapis.com/css2?family=Roboto:wght@400;500;700&family=Open+Sans:wght@600&display=swap">
<style>
  :root {
    --page: #d2d2d2;
    --navy: #2b2f85;
    --ink: #23257a;
    --accent: #1a78c2;
    --band: #0a6fba;
    --icon: #1ea3de;
    --ring: #b8b8b8;
    --glow: #19aceb;
    --deep: #2e3592;
    --white: #ffffff;
  }
  * { margin: 0; padding: 0; box-sizing: border-box; }
  html, body { width: 900px; height: 1200px; overflow: hidden; }
  body { background: var(--page); font-family: "Roboto", Arial, sans-serif; position: relative; }

  .card { position: absolute; left: 137px; width: 620px; overflow: hidden; }
  .card-front { top: 161px; height: 409px; background: var(--white); }
  .card-back {
    top: 637px; height: 410px;
    background: radial-gradient(circle at 200px 175px, var(--glow) 0%, #0a8ad6 25%, #0561b4 48%, var(--deep) 75%);
  }

  .holder { position: absolute; left: 48px; top: 42px; }
  .holder-name { font-size: 22px; font-weight: 500; color: var(--ink); line-height: 1; }
  .holder-title { font-size: 19px; color: var(--accent); margin-top: 6px; line-height: 1; }
  .address { font-size: 14px; color: var(--ink); line-height: 18px; margin-top: 14px; }
  .contacts { list-style: none; margin-top: 14px; }
  .contacts li { display: flex; align-items: center; font-size: 14.5px; color: var(--ink); height: 20px; }
  .contacts svg { width: 13px; height: 13px; margin-right: 9px; fill: var(--icon); }

  .brand { position: absolute; left: 420px; top: 48px; width: 160px; text-align: center; }
  .brand-ring { display: block; margin: 0 auto; }
  .brand-name { font-family: "Open Sans", Arial, sans-serif; font-weight: 600; font-size: 13px; line-height: 18px; color: var(--ink); margin-top: 8px; }

  .rule-top { position: absolute; left: 0; top: 247px; width: 100%; height: 4px; background: var(--navy); }
  .band { position: absolute; left: 0; top: 256px; width: 100%; height: 134px; background: var(--band); }
  .rule-bottom { position: absolute; left: 0; top: 395px; width: 100%; height: 14px; background: var(--navy); }

  .partner { position: absolute; top: 18px; text-align: center; color: var(--white); }
  .partner-a { left: 108px; width: 190px; }
  .partner-b { left: 318px; width: 176px; }
  .partner-mark { display: flex; align-items: center; justify-content: center; gap: 8px; height: 60px; }
  .partner-mark span { font-weight: 700; font-size: 12px; line-height: 14px; text-align: left; }
  .partner-mark i { display: block; width: 56px; height: 56px; border-radius: 50%; background: var(--white); flex: none; }
  .partner-b .partner-mark i { background: none; border: 2px solid var(--white); }
  .partner-place { font-size: 13px; font-weight: 500; line-height: 17px; margin-top: 8px; letter-spacing: .2px; }

  .back-brand { position: absolute; left: 140px; top: 128px; display: flex; align-items: center; gap: 22px; }
  .back-ring { width: 122px; height: 122px; border: 2.5px solid var(--white); border-radius: 50%; }
  .back-name { font-family: "Open Sans", Arial, sans-serif; font-weight: 600; font-size: 20px; line-height: 30px; color: var(--white); text-align: center; }
</style>
</head>
<body>

<section class="card card-front">
  <div class="holder">
    <h1 class="holder-name">Daniel Harwell</h1>
    <p class="holder-title">Attorney</p>
    <p class="address">No.7, 2nd Sarv Baghestan-e-Nouri<br>Tehran, IR</p>
    <ul class="contacts">
      <li><svg viewBox="0 0 16 16"><path d="M3 1l3 3-1.5 2c1 2 3 4 5 5L11.5 9.5l3 3-2 2.5C7 14 2 9 1 3z"/></svg>+98 21 66394512</li>
      <li><svg viewBox="0 0 16 16"><path d="M1 4c2-2 12-2 14 0v2h-4V5H5v1H1zM3 8h10l1 6H2zM5 10h2v1H5zm4 0h2v1H9z"/></svg>+98 21 66395830</li>
      <li><svg viewBox="0 0 16 16"><path d="M1 3h14v10H1zM2 4v1l6 4 6-4V4z"/></svg>info@roshanbarsaz.com</li>
      <li><svg viewBox="0 0 16 16"><path d="M8 1a7 7 0 110 14A7 7 0 018 1zm0 1.5C6.8 4 6.3 6 6.3 8s.5 4 1.7 5.5C9.2 12 9.7 10 9.7 8S9.2 4 8 2.5zM2.6 7.3h10.8v1.4H2.6z"/></svg>www.roshanbarsaz.com</li>
    </ul>
  </div>

  <div class="brand">
    <svg class="brand-ring" width="130" height="130" viewBox="0 0 130 130"><circle cx="65" cy="65" r="62" fill="none" stroke="var(--ring)" stroke-width="3"/></svg>
    <p class="brand-name">Roshan Barsaz<br>International<br>Transport.Co L.Lc</p>
  </div>

  <div class="rule-top"></div>
  <div class="band">
    <div class="partner partner-a">
      <div class="partner-mark"><i></i><span>CALM REEF<br>SHIPPING LLC</span></div>
      <p class="partner-place">Dubai, United Arab Emirates<br>www.crsuae.com</p>
    </div>
    <div class="partner partner-b">
      <div class="partner-mark"><i></i><span>TQM<br>Shipping Line Ltd</span></div>
      <p class="partner-place">London, United Kingdom<br>www.tqmline.com</p>
    </div>
  </div>
  <div class="rule-bottom"></div>
</section>

<section class="card card-back">
  <div class="back-brand">
    <div class="back-ring"></div>
    <p class="back-name">Roshan Barsaz<br>International<br>Transport.Co L.Lc</p>
  </div>
</section>

</body>
</html>
```